Business Card Design and Signature

Hi there,

I have just started my own business which does interior make overs. I am looking for a new business card that I can give to customers and people that I meet. I would like my business card to include a logo design, colour theme and font that reflects a modern, fresh, casual, warm and friendly feeling. My target customers are mid aged home owners who are looking to freshen up their homes.

I would like the design to translate into my email signature

Requirements
Sides: Front and back business card design
Size: email footer

Content to include:
* Name
* Phone
* email
* website
* strap line: Rooms Made Warm

Please look at options such as:
* with some type of graphic
* with or without a photo of me
* variations on edge style such as rounded
* a font that I could then use in my website for continuity
* a colour style that I could then use in my website again for continuity

will require all files to give to printer and apply to my email applcation

Thanks

Bea

```html
<!DOCTYPE html>
<html lang="en">
<head>
<meta charset="utf-8">
<title>Nestwell Business Card</title>
<link href="https://fonts.googleapis.com/css2?family=Montserrat:wght@400;600;700;800&display=swap" rel="stylesheet">
<style>
  :root {
    --page: #e9ecef;
    --brand-blue: #13b6d8;
    --brand-blue-deep: #0fa3c6;
    --ink: #1d1d1f;
    --muted: #7a7f85;
    --paper: #ffffff;
  }
  * { box-sizing: border-box; margin: 0; padding: 0; }
  html, body {
    width: 1200px; height: 900px; overflow: hidden;
    background: var(--page);
    font-family: "Montserrat", sans-serif;
  }
  .card-sheet {
    width: 1200px; height: 900px;
    display: flex; align-items: center; justify-content: center; gap: 60px;
  }
  .card {
    position: relative;
    width: 525px; height: 300px;
    border-radius: 26px;
    overflow: hidden;
    box-shadow: 0 10px 30px rgba(0,0,0,0.12);
  }
  /* Front */
  .card--front {
    background: linear-gradient(135deg, var(--brand-blue) 0%, var(--brand-blue-deep) 100%);
    display: flex; align-items: center; justify-content: center;
    color: var(--paper);
  }
  .front-brand { display: flex; flex-direction: column; align-items: flex-start; }
  .brand-row { display: flex; align-items: center; gap: 14px; }
  .brand-mark {
    width: 38px; height: 38px; background: var(--paper); border-radius: 4px;
  }
  .brand-name {
    font-weight: 700; font-size: 44px; letter-spacing: 1px; line-height: 1;
  }
  .front-tagline {
    font-weight: 400; font-size: 21px; margin-top: 6px; margin-left: 52px;
  }
  /* Back */
  .card--back { background: var(--paper); }
  .swoosh { position: absolute; inset: 0; }
  .holder { position: absolute; left: 34px; top: 30px; }
  .holder-name {
    color: var(--brand-blue); font-weight: 800; font-size: 24px; letter-spacing: 0.5px;
  }
  .holder-title { color: var(--muted); font-weight: 600; font-size: 14px; letter-spacing: 1px; margin-top: 2px; }
  .back-brand { position: absolute; left: 34px; top: 110px; }
  .back-brand .brand-row { gap: 10px; }
  .back-brand .brand-mark { width: 24px; height: 24px; background: var(--brand-blue); border-radius: 3px; }
  .back-brand .brand-name { color: var(--ink); font-size: 26px; }
  .back-brand .back-tagline { color: var(--ink); font-size: 11px; font-weight: 400; margin-left: 34px; margin-top: 3px; }
  .contact-list {
    position: absolute; right: 30px; bottom: 40px;
    list-style: none; text-align: right;
  }
  .contact-item {
    display: flex; align-items: center; justify-content: flex-end; gap: 12px;
    font-size: 13px; color: var(--ink); line-height: 1.25; margin-top: 9px;
  }
  .contact-icon { width: 14px; height: 14px; flex: none; fill: var(--ink); }
</style>
</head>
<body>
<main class="card-sheet">
  <section class="card card--front" aria-label="Card front">
    <div class="front-brand">
      <div class="brand-row">
        <span class="brand-mark"></span>
        <span class="brand-name">NESTWELL</span>
      </div>
      <p class="front-tagline">Rooms Made Warm</p>
    </div>
  </section>

  <section class="card card--back" aria-label="Card back">
    <svg class="swoosh" viewBox="0 0 525 300" preserveAspectRatio="none" aria-hidden="true">
      <path d="M525 42 C 380 52, 300 97, 262 160 C 226 218, 170 242, 0 264 L 0 268 C 174 250, 234 224, 267 166 C 304 104, 384 60, 525 47 Z" fill="var(--brand-blue)"/>
    </svg>

    <div class="holder">
      <h1 class="holder-name">MARA QUILL</h1>
      <p class="holder-title">Your Subtitle Here</p>
    </div>

    <div class="back-brand">
      <div class="brand-row">
        <span class="brand-mark"></span>
        <span class="brand-name">NESTWELL</span>
      </div>
      <p class="back-tagline">Rooms Made Warm</p>
    </div>

    <ul class="contact-list">
      <li class="contact-item">+000 555 210 348
        <svg class="contact-icon" viewBox="0 0 24 24"><path d="M6.6 10.8a15.1 15.1 0 0 0 6.6 6.6l2.2-2.2c.3-.3.7-.4 1-.2 1.1.4 2.3.6 3.6.6.6 0 1 .4 1 1V20c0 .6-.4 1-1 1A17 17 0 0 1 3 4c0-.6.4-1 1-1h3.5c.6 0 1 .4 1 1 0 1.3.2 2.5.6 3.6.1.3 0 .7-.2 1z"/></svg>
      </li>
      <li class="contact-item">hello@nestwell.com
        <svg class="contact-icon" viewBox="0 0 24 24"><path d="M2 5h20v14H2z M4 7v.5l8 5 8-5V7l-8 5z" fill-rule="evenodd"/></svg>
      </li>
      <li class="contact-item">www.nestwell.com
        <svg class="contact-icon" viewBox="0 0 24 24"><circle cx="12" cy="12" r="10"/><path d="M2 12h20M12 2c3 3 3 17 0 20M12 2c-3 3-3 17 0 20" stroke="#fff" stroke-width="1.5" fill="none"/></svg>
      </li>
      <li class="contact-item"><span>42 Linden Court Road 8<br>Fairmont AC 30218</span>
        <svg class="contact-icon" viewBox="0 0 24 24"><path d="M12 2a7 7 0 0 0-7 7c0 5 7 13 7 13s7-8 7-13a7 7 0 0 0-7-7zm0 9.5a2.5 2.5 0 1 1 0-5 2.5 2.5 0 0 1 0 5z"/></svg>
      </li>
    </ul>
  </section>
</main>
</body>
</html>
```